Payroll Brochure

Create a brochure with the copy i have provided . A simple easy tp read brochure that shows wat we do we handle payroll taxes insurance 401k etc

```html
<!DOCTYPE html>
<html lang="en">
<head>
<meta charset="utf-8">
<title>Norvale – Payroll &amp; HR Services Brochure</title>
<link href="https://fonts.googleapis.com/css2?family=Outfit:wght@300;400;500;600;700&display=swap" rel="stylesheet">
<style>
  :root {
    --backdrop: #c6c6c6;
    --paper: #f1f1f1;
    --brand-red: #6a0a0c;
    --heading-red: #7a1216;
    --spine-type: #c9777a;
    --ink: #2a2a2a;
    --ink-strong: #111111;
  }
  * { box-sizing: border-box; margin: 0; padding: 0; }
  html, body {
    width: 1200px; height: 1000px; overflow: hidden;
    background: var(--backdrop);
    font-family: "Outfit", sans-serif;
    color: var(--ink);
  }
  .spread {
    position: absolute; left: 0; top: 76px;
    width: 1200px; height: 847px;
    background: var(--paper);
  }
  .block { position: absolute; }
  .section-title {
    font-size: 13.5px; font-weight: 600; color: var(--heading-red);
    letter-spacing: 0.1px; text-transform: uppercase; white-space: nowrap;
  }
  .section-title.lead-title { font-size: 11.6px; letter-spacing: -0.1px; }
  .copy {
    font-size: 10.2px; font-weight: 300; line-height: 12.3px;
    text-align: justify; color: var(--ink);
  }
  .copy b { font-weight: 600; color: var(--ink-strong); }
  .feature {
    font-size: 10.6px; font-weight: 600; line-height: 13.3px;
    text-align: justify; color: var(--ink-strong);
  }
  .feature .label { font-weight: 700; }
  .label-small { font-size: 9.8px; font-weight: 600; color: var(--ink-strong); }
  .accent-bar {
    position: absolute; left: 39px; top: 79px;
    width: 6px; height: 150px; background: var(--brand-red);
  }
  .spine {
    position: absolute; left: 542px; top: 0;
    width: 58px; height: 847px; background: var(--brand-red);
  }
  .spine svg { display: block; }
  .photo-band {
    position: absolute; left: 658px; top: 205px;
    width: 481px; height: 102px;
    background: linear-gradient(100deg, #8c3b3d 0%, #c98a8b 35%, #f3e6e6 55%, #e9cfcf 75%, #93484a 100%);
  }
  .left-col { left: 60px; width: 423px; }
  .right-col { left: 660px; width: 479px; }
</style>
</head>
<body>
<main class="spread">

  <!-- Left page -->
  <div class="accent-bar"></div>

  <h2 class="block section-title lead-title" style="top:53px; left:62px;">What makes Norvale uniquely qualified to be your service provider?</h2>

  <p class="block copy left-col" style="top:87px;"><b>People:</b> Norvale has gone to great lengths to hire and train a world-class team of experienced payroll and HR professionals that are genuinely interested in making sure our clients receive the very best in service and support.</p>
  <p class="block copy left-col" style="top:136px;"><b>Process:</b> Developed over the years, the Norvale process has been designed with speed and accuracy in mind. Norvale does what’s needed to make sure our clients are presented with speedy responses to their questions, and produce accurate, reliable, and timely payrolls. With Norvale’s custom designed software, we can easily tailor to your payroll needs.</p>
  <p class="block copy left-col" style="top:196px;"><b>Products:</b> Norvale has developed a comprehensive suite of products and services that will fit your needs.</p>
  <p class="block copy left-col" style="top:232px;"><b>Flexibility:</b> Norvale will design HR solutions that meet your specific needs and requirements.</p>

  <h2 class="block section-title" style="top:278px; left:62px;">Payroll Management</h2>

  <p class="block feature left-col" style="top:312px;"><span class="label">Flexible -</span><br>NORVALE’S flexible and powerful payroll module allows you the ability to grow you’re your business by meeting your unique needs. Supporting payrolls for very large to very small companies,</p>
  <p class="block feature left-col" style="top:379px;"><span class="label">Efficient -</span><br>Get payroll done efficiently and accurately by relying on our flexible design to handle even the most complex payroll needs.</p>
  <p class="block feature left-col" style="top:432px;"><span class="label">Grow without Growing Pains -</span><br>NORVALE’S technology and design is able to allow you to scale your business without adding all the incremental costs typically required.</p>

  <h2 class="block section-title" style="top:505px; left:62px;">Tax Reporting &amp; Payments</h2>

  <p class="block label-small" style="top:538px; left:60px;">Accurate :</p>
  <p class="block copy" style="top:563px; left:60px; width:183px;">All payroll taxes (federal, state, local) are calculated accurately. Additionally, we determine proper local tax jurisdictions based on the employee home and work addresses.</p>
  <p class="block label-small" style="top:538px; left:302px;">Complete :</p>
  <p class="block copy" style="top:563px; left:302px; width:181px;">Federal, State, and Local withholding taxes as well as State and Federal Unemployment taxes are provided. Tax payments are integrated into the Accounts Payable and General Ledger modules.</p>

  <h2 class="block section-title" style="top:663px; left:62px;">Human Resources</h2>

  <p class="block copy left-col" style="top:699px;"><b>With</b> our online HR tools, you can empower yourself to take control of your human resource needs or let us do it.</p>
  <p class="block copy left-col" style="top:735px;"><b>Get Big Company Services :</b> By using our online tools in conjunction with your service team, you will have access to HR services only afforded by some of the largest companies.</p>
  <p class="block copy left-col" style="top:772px;"><b>Library :</b> our online document library lets you and employees create your own library of information accessible at any time. Employees can upload documents and forms that can be kept in history as long as needed.</p>

  <!-- Spine -->
  <div class="spine">
    <svg width="58" height="847" viewBox="0 0 58 847" aria-label="Payroll, Taxes, Benefits">
      <text x="0" y="0" transform="translate(17 46) rotate(90)" textLength="756" lengthAdjust="spacing"
            font-family="Outfit, sans-serif" font-size="30" font-weight="300"
            fill="var(--spine-type)">PAYROLL · TAXES · BENEFITS</text>
    </svg>
  </div>

  <!-- Right page -->
  <h2 class="block section-title" style="top:52px; left:661px;">Benefit Enrollment</h2>

  <p class="block copy right-col" style="top:86px;"><b>Easy and Quick Enrollment :</b> Our intuitive user experience quickly walks employees through their benefit enrollment process and allows them to compare different plans and select those that best meet their life needs.</p>
  <p class="block copy right-col" style="top:134px;"><b>Flexible Benefit Plans and Easy Setup Options :</b> Offer your clients Top-Tier benefit plans or administer their plans in an easy to use, yet flexible benefit administration module.</p>
  <p class="block copy right-col" style="top:171px;"><b>You Pick :</b> With our flexible contribution setup features, you can contribute in any manner to your employees’ benefits while the system automatically processes them through payroll.</p>

  <div class="photo-band" role="img" aria-label="Red-toned photo of a hand passing a pen over a document to clasped hands"></div>

  <h2 class="block section-title" style="top:338px; left:660px;">On Boarding</h2>

  <p class="block copy right-col" style="top:373px;"><b>Customize your On Boarding :</b> you can customize your on boarding experience to your hiring needs as well as provide multiple workflows for different employee types. The on boarding experience can be branded for you, providing a personalized experience for the employees.</p>
  <p class="block copy right-col" style="top:421px;"><b>Custom Document Management :</b> our custom document mapping feature lets you use your own forms and documents as part of the on boarding and hiring process. When these forms are completed – and electronically signed – they stay in history as long as needed.</p>
  <p class="block copy right-col" style="top:470px;"><b>Intuitive :</b> with a focus on the user experience, your employees will find it easy and quick to get on boarded with you.</p>

  <h2 class="block section-title" style="top:522px; left:661px;">Applicant Tracking</h2>

  <p class="block copy right-col" style="top:558px;"><b>Create and Post Jobs :</b> you can create jobs with just a few clicks and post them on all the popular job sites.</p>
  <p class="block copy right-col" style="top:594px;"><b>Hire the Right People :</b> by posting on popular job boards, as well as a proprietary database of job seekers, you will reach more candidates. You can choose to receive profiles of candidates that only match your background and specifications.</p>
  <p class="block copy right-col" style="top:643px;"><b>Manage the Hiring Process :</b> review candidates via video or online conferencing, review voice interviews, schedule in person interviews, have candidates answer certain online questions, and manage this entire process to find the right people. Once hired, they can be on boarded automatically.</p>

  <h2 class="block section-title" style="top:701px; left:661px;">Time and Attendance</h2>

  <p class="block label-small" style="top:736px; left:661px;">Make Time Entry Easy :</p>
  <p class="block copy" style="top:760px; left:661px; width:133px;">Simplify time tracking so you can spend less time on payroll tasks.</p>
  <p class="block label-small" style="top:736px; left:834px;">Everywhere Access :</p>
  <p class="block copy" style="top:760px; left:834px; width:133px; text-align:left;">Web interface, mobile apps, and on-premise time clocks allow employees to log their time wherever they are.</p>
  <p class="block label-small" style="top:736px; left:1007px;">Plug and Play Time Clocks :</p>
  <p class="block copy" style="top:760px; left:1007px; width:134px;">Time clocks are delivered ready-to-use with little or no setup required.</p>

</main>
</body>
</html>
```